Marlow Aviation Group Envelope, Letterhead, Business Card Design

I need designs for a new company letterhead, business cards, and envelopes. These designs will need to be presented using 5 different company logos for the different divisions that are managed under the Marlow Aviation Group umbrella (company names listed below). The member of FRCU logo should also be included.
- Marlow Aviation Group
- Marlow Jet Management
- Marlow Jet Charter
- Marlow Pilot Services
- Marlow Aircraft Sales
- Marlow Flight Training

Logos for the various companies are attached as well as a screen shot of the main page of our website.

```html
<!DOCTYPE html>
<html lang="en">
<head>
<meta charset="utf-8">
<title>Marlow Aircraft Sales Stationery</title>
<link rel="stylesheet" href="https://fonts.googleapis.com/css2?family=Josefin+Slab:wght@400;600&family=Open+Sans:wght@400;700&display=swap">
<style>
  :root {
    --backdrop: #d8d8d8;
    --paper: #f7f7f7;
    --cobalt: #0a60b0;
    --ink: #111111;
    --body-text: #4a4a4a;
    --muted: #555555;
  }
  * { box-sizing: border-box; margin: 0; padding: 0; }
  html, body { width: 1200px; height: 900px; overflow: hidden; }
  body { background: var(--backdrop); position: relative; font-family: "Open Sans", sans-serif; }

  .wordmark {
    color: var(--cobalt);
    font-family: "Open Sans", sans-serif;
    font-weight: 700;
    text-transform: uppercase;
    text-align: center;
    line-height: 1.05;
    letter-spacing: 0.04em;
  }

  .letterhead {
    position: absolute; left: 278px; top: 98px; width: 494px; height: 695px;
    background: var(--paper);
    box-shadow: 0 1px 3px rgba(0,0,0,0.12);
  }
  .letterhead .wordmark { position: absolute; left: 130px; top: 66px; width: 234px; font-size: 22px; }
  .letterhead .wordmark small { display: block; font-size: 13px; letter-spacing: 0.08em; }
  .letter-body {
    position: absolute; left: 70px; top: 213px; width: 355px;
    font-family: "Josefin Slab", serif; font-size: 9.2px; line-height: 12.4px;
    color: var(--body-text); text-align: justify; hyphens: auto;
  }
  .letter-body p { margin-bottom: 12.4px; }
  .stripe { position: absolute; height: 15px; }
  .letterhead .stripe-blue { left: 0; top: 669px; width: 404px; background: var(--cobalt); }
  .letterhead .stripe-black { left: 414px; top: 669px; width: 80px; background: var(--ink); }

  .card {
    position: absolute; background: #ffffff;
    box-shadow: 0 2px 6px rgba(0,0,0,0.18);
  }
  .card-front { left: 845px; top: 99px; width: 207px; height: 128px; }
  .card-front .wordmark { position: absolute; left: 20px; top: 45px; width: 167px; font-size: 17px; }
  .card-front .wordmark small { display: block; font-size: 10px; letter-spacing: 0.08em; }

  .card-back { left: 849px; top: 265px; width: 201px; height: 129px; }
  .card-back .wordmark { position: absolute; left: 40px; top: 32px; width: 121px; font-size: 12px; }
  .card-back .wordmark small { display: block; font-size: 7px; letter-spacing: 0.08em; }
  .holder { position: absolute; left: 12px; top: 86px; width: 80px; text-align: center; }
  .holder-name { font-weight: 700; font-size: 7.5px; color: #333; }
  .holder-role { font-size: 5px; color: var(--muted); letter-spacing: 0.03em; }
  .contact { position: absolute; left: 105px; top: 80px; list-style: none; font-size: 3.6px; color: #333; }
  .contact li { display: flex; align-items: center; height: 7.6px; }
  .contact svg { width: 4px; height: 4px; margin-right: 3px; fill: #333; }
  .contact .label { width: 27px; text-transform: uppercase; }
  .card-back .stripe-blue { left: 0; top: 116px; width: 161px; height: 7px; background: var(--cobalt); }
  .card-back .stripe-black { left: 175px; top: 116px; width: 26px; height: 7px; background: var(--ink); }

  .logo-standalone { position: absolute; left: 862px; top: 568px; width: 290px; font-size: 40px; }
  .logo-standalone small { display: block; font-size: 21px; letter-spacing: 0.08em; }
</style>
</head>
<body>

  <section class="letterhead" aria-label="Letterhead">
    <div class="wordmark">Marlow<small>Aircraft Sales</small></div>
    <div class="letter-body">
      <p>Lorem ipsum dolor sit amet,</p>
      <p>Lorem ipsum dolor sit amet, consectetur adipiscing elit. Donec orci purus, luctus vitae dignissim eu, iaculis sed purus. Vivamus faucibus, ipsum nec aliquet viverra, leo mauris condimentum ligula, sit amet sagittis enim ligula quis arcu. Nam egestas tortor id nisi porttitor mattis. In tortor ante, ultricies in suscipit a, tempus non massa. Vivamus et auctor mi. Fusce vel massa nulla. Phasellus nec eros mauris, et scelerisque orci. Donec malesuada orci vitae nulla accumsan porta a id massa. Quisque accumsan iaculis magna sit amet fringilla. Maecenas consequat, magna eget tincidunt semper, odio nibh rutrum mi, id feugiat ante nisi eu risus. Vestibulum nunc orci, rhoncus a placerat in, ultricies in mi. Cras mattis varius eros, vel fringilla nisi suscipit eget.</p>
      <p>Quisque scelerisque sagittis nulla at porttitor. Mauris a justo et tellus interdum tristique. Sed id augue vitae urna euismod commodo aliquet a quam. Pellentesque arcu velit, cursus et malesuada ut, consequat et diam. Nullam erat sem, rhoncus id ullamcorper vitae, rhoncus et arcu. In ultricies ultricies nulla, ut rutrum nisi iaculis at. Donec eu magna a metus ornare faucibus. Fusce aliquet faucibus ultricies. Morbi semper, est id tincidunt gravida, sem arcu adipiscing lacus, ac bibendum nulla leo eu purus. Quisque nec diam sed risus consectetur a ccumsan quis quis nibh. Vestibulum id purus lorem.</p>
      <p>Vivamus vehicula accumsan lacinia. Aliquam erat volutpat. Pellentesque consequat venenatis velit non gravida. Etiam et sem et nulla congue aliquam sed eget augue. Nulla facilisi. Pellentesque habitant morbi tristique senectus et netus et malesuada fames ac turpis egestas. Nulla a elit at sem iaculis congue. Nullam mollis tristique lobortis.</p>
    </div>
    <div class="stripe stripe-blue"></div>
    <div class="stripe stripe-black"></div>
  </section>

  <section class="card card-front" aria-label="Business card front">
    <div class="wordmark">Marlow<small>Aircraft Sales</small></div>
  </section>

  <section class="card card-back" aria-label="Business card back">
    <div class="wordmark">Marlow<small>Aircraft Sales</small></div>
    <div class="holder">
      <div class="holder-name">Daniel Reyes</div>
      <div class="holder-role">GRAPHIC DESIGNER</div>
    </div>
    <ul class="contact">
      <li><svg viewBox="0 0 10 10"><path d="M5 0a3.5 3.5 0 0 0-3.5 3.5C1.5 6 5 10 5 10s3.5-4 3.5-6.5A3.5 3.5 0 0 0 5 0zm0 5a1.5 1.5 0 1 1 0-3 1.5 1.5 0 0 1 0 3z"/></svg><span class="label">Address</span><span>Harbor Lane 214</span></li>
      <li><svg viewBox="0 0 10 10"><rect x="2.5" y="0" width="5" height="10" rx="1"/></svg><span class="label">Phone</span><span>+00 555 0147 2286</span></li>
      <li><svg viewBox="0 0 10 10"><rect x="0" y="2" width="10" height="6"/></svg><span class="label">Email</span><span>dreyes@mail.com</span></li>
      <li><svg viewBox="0 0 10 10"><path d="M5 0 0 5h1.5v5h7V5H10z"/></svg><span class="label">Website</span><span>http://www.marlowsales.com</span></li>
    </ul>
    <div class="stripe stripe-blue"></div>
    <div class="stripe stripe-black"></div>
  </section>

  <div class="wordmark logo-standalone">Marlow<small>Aircraft Sales</small></div>

</body>
</html>
```